Security Company Needs a Website *

We need a website that gives our clients information about the services we provide, methods of contacting us and landing page to advertise on social media sites.

We need five landing pages titled Home, About Us, Services, Contact Us and a Landing Page that can be linked to Chatterloop advertising.

About Us - Should have a section for Core Values & Ethics, Our Vision, Our Mission and Partners.

Services - This page should show the different categories which include CCTV, Security Alarms, Access Control and Fire Protection.

CCTV Service Description:
Closed circuit television (CCTV) has long been implemented by businesses as a surveillance tool in areas that need monitoring. With digital CCTV cameras, multiple video cameras transmit signals through a set of monitors. The cameras provide thorough surveillance of the area.

With vast technological improvements over the last ten years, businesses with CCTV systems can use unique IP cameras and video analytics to monitor traffic flows, people-count, implement facial and number plate recognition. Useful information about customer behaviour and demographics can be discovered too. CCTV helps prevent crime in many industries and can assist with the improvement of industrial processes, safety on transport systems and traffic monitoring.

Security Alarms Service Description:
Alarms systems are electronic devices programmed to alert people to specific dangers and detect intrusions, fire or theft. Security alarms, systems and access control monitoring combine to create an integrated surveillance solution, tailored to your business’ unique requirements. Our surveillance and alarm monitoring services are ideal for perimeter protection from unwanted intruders or potential dangers.

Access Control Services:
An access control system allows for the free flow of authorised personnel while denying entry to unwanted visitors. With walk-in thieves and trespassers shut out, you dramatically reduce your exposure to crime while increasing the security of your employees, visitors, information and assets.

* Control when and who is entering your premises
* Protect employees, assets and information
* Secure an area or sector
* Observe movement
* Integrate with other security systems

Our range of access control systems can be seamlessly linked to other systems in our portfolio. These include Fire Detection Systems, Intruder Alarms, CCTV, and Building Management. A common request involves the need for a CCTV camera to pan around and focus on a door that has been highlighted as a security risk by the access control system.

Fire Protection Service:
To Be Advised

The above copy-writing will also have to be changed.

Contact Us - This form needs to be simple and straightforward to gather the prospects information and we would like to have a call to action on this page. The Contact Us page should also have a wayfindr charts location of our office address.

We would also like to have a link to our chatterloop page on the website.

Target Market(s)

Commercial businesses, building construction developers and property managers.

Industry/Entity Type

Security

Number of Pages Required

5+ page

Font styles to use
Sans Serif

Colors

Designer to choose colors to be used in the design.

Requirements
Must have
• We need to have the same look and feel as well as website features as the following website:
• https://www.kelvaguard.example.au/business-security/
• The website must be easy to use and easy to edit as well.

```html
<!DOCTYPE html>
<html lang="en">
<head>
<meta charset="utf-8">
<title>Lumora Security Solutions – Business Security</title>
<link href="https://fonts.googleapis.com/css2?family=Open+Sans:wght@300;400;600;700&display=swap" rel="stylesheet">
<style>
:root{
  --blue:#1a63c9;
  --blue-deep:#0f4ca8;
  --blue-band:#1559c0;
  --ink:#2b2e33;
  --text:#6d7178;
  --dark-bar:#2b2d31;
  --mint:#e5f2ef;
  --sky:#e3edf6;
  --page:#f4f6f9;
  --card:#f3f4f6;
  --field-line:#cfd3d8;
  --white:#ffffff;
}
*{box-sizing:border-box;margin:0;padding:0}
html,body{width:1200px;height:4412px;overflow:hidden}
body{font-family:"Open Sans",Arial,sans-serif;color:var(--ink);background:var(--page);position:relative}
.abs{position:absolute}

/* header */
.site-header{position:absolute;left:0;top:0;width:1200px;height:110px;background:rgba(255,255,255,.96);z-index:3}
.brand{position:absolute;left:88px;top:18px;display:flex;align-items:center;gap:10px}
.brand-mark{width:70px;height:70px;border-radius:50%;background:var(--blue-deep)}
.brand-name{font-size:13px;font-weight:600;color:var(--blue-deep);line-height:1.25;width:130px}
.main-nav{position:absolute;left:448px;top:44px;display:flex;gap:34px;font-size:14px;font-weight:600;letter-spacing:.5px}
.main-nav a{color:var(--ink);text-decoration:none}
.main-nav a.active{color:var(--blue);border-bottom:2px solid var(--blue);padding-bottom:8px}
.call-btn{position:absolute;left:832px;top:40px;height:30px;width:190px;text-align:center;border-radius:15px;background:var(--blue);color:#fff;font-size:13px;font-weight:600;line-height:30px}
.social{position:absolute;left:1045px;top:38px;display:flex;gap:14px}
.social span{width:34px;height:34px;border-radius:50%;background:var(--blue-deep);display:block}

/* hero */
.hero{position:absolute;left:0;top:0;width:1200px;height:603px;background:linear-gradient(100deg,#1c3f86 0%,#2a5fb3 45%,#5b87c9 75%,#3d6bb4 100%)}
.hero-title{position:absolute;left:153px;top:252px;font-size:44px;font-weight:600;color:#fff;letter-spacing:.5px}
.hero-copy{position:absolute;left:153px;top:318px;width:500px;font-size:19px;line-height:1.25;color:#fff}
.outline-btn{position:absolute;height:32px;padding:0 22px;border:2px solid #fff;border-radius:16px;color:#fff;font-size:12px;font-weight:600;line-height:28px;letter-spacing:.5px}
.hero-arrow{position:absolute;top:336px;width:40px;height:40px;background:#fff;border-radius:3px}
.hero-arrow svg{display:block;margin:10px}

/* support bar */
.support-bar{position:absolute;left:0;top:603px;width:1200px;height:97px;background:var(--dark-bar);color:#fff}
.support-bar h3{position:absolute;left:234px;top:22px;font-size:19px;font-weight:600}
.support-bar p{position:absolute;left:234px;top:52px;font-size:13px;color:#c9ccd1}
.support-call{position:absolute;left:790px;top:22px;font-size:21px;color:#5aa0f2}
.support-mail{position:absolute;left:790px;top:56px;font-size:13px;color:#5aa0f2}

/* about */
.about-backer{position:absolute;left:170px;top:782px;width:442px;height:366px;background:var(--blue)}
.about-photo{position:absolute;left:126px;top:756px;width:462px;height:370px;background:linear-gradient(135deg,#d9dde3,#9aa7b8 60%,#e8ecf0)}
.about h2{position:absolute;left:661px;top:770px;font-size:30px;font-weight:400;color:var(--ink)}
.about h2 b,.section-title b{color:var(--blue);font-weight:600}
.about p{position:absolute;left:661px;width:390px;font-size:12.5px;line-height:17px;color:var(--text);text-align:justify}
.blue-btn{position:absolute;height:32px;padding:0 28px;border:2px solid var(--blue);border-radius:16px;color:var(--blue-deep);font-size:11px;font-weight:600;line-height:28px;letter-spacing:.5px;background:#fff}

.section-title{position:absolute;left:0;width:1200px;top:1282px;text-align:center;font-size:30px;font-weight:400}

/* services */
.service-row{position:absolute;left:0;width:1200px;height:403px;background:#fff}
.service-text{position:absolute;top:0;width:600px;height:403px}
.service-text.mint{background:var(--mint)}
.service-text.sky{background:var(--sky)}
.service-text h3{position:absolute;top:92px;font-size:29px;font-weight:400;color:var(--blue-deep)}
.service-text .rule{position:absolute;top:86px;height:2px;background:var(--blue)}
.service-text p{position:absolute;top:156px;width:430px;font-size:12px;line-height:19px;color:var(--text)}
.service-text .blue-btn{top:280px;background:transparent}
.service-text.fire h3{top:62px}
.service-text.fire .rule{top:56px}
.service-text.fire p{top:124px}
.service-text.fire .blue-btn{top:318px}
.service-photo{position:absolute}

/* features */
.feature{position:absolute;top:3098px;width:220px;text-align:center}
.feature-icon{width:124px;height:124px;margin:0 auto;border-radius:50%;border:2px solid var(--ink);background:#fff;display:flex;align-items:center;justify-content:center}
.feature-icon.primary{background:var(--blue);border:8px solid #d3e2f6}
.feature h4{margin-top:24px;font-size:18px;font-weight:600;color:var(--ink)}
.feature h4.accent{color:var(--blue)}
.dash{position:absolute;top:3160px;height:0;border-top:2px dashed #9aa0a8}

/* cta band */
.cta-band{position:absolute;left:0;top:3322px;width:1200px;height:244px;background:linear-gradient(180deg,var(--blue-band),var(--blue-deep));color:#fff;text-align:center}
.cta-band h2{margin-top:62px;font-size:31px;font-weight:400}
.cta-band p{margin-top:10px;font-size:13px}

.map-area{position:absolute;left:0;top:3566px;width:1200px;height:374px;background:linear-gradient(120deg,#dfe3e0 0%,#d4dad6 55%,#b9cfe6 70%,#a9c3e0 100%)}
.blue-foot{position:absolute;left:0;top:3940px;width:1200px;height:472px;background:linear-gradient(180deg,#1b5cc0,#1752b2)}

/* contact */
.contact-card{position:absolute;left:153px;top:3860px;width:894px;height:388px;background:var(--card);box-shadow:0 6px 20px rgba(0,0,0,.2)}
.contact-card h2{position:absolute;left:0;width:100%;top:26px;text-align:center;font-size:30px;font-weight:400;color:var(--ink)}
.contact-card .lead{position:absolute;left:0;width:100%;top:72px;text-align:center;font-size:13px;color:var(--text)}
.field{position:absolute;height:34px;background:#fff;border:1px solid var(--field-line);font-size:12px;color:#9a9ea5;padding:8px 10px}
.field.message{height:118px}
.send-btn{position:absolute;left:384px;top:330px;height:34px;width:128px;text-align:center;border:2px solid var(--blue);border-radius:17px;color:var(--blue-deep);font-size:11px;font-weight:600;line-height:30px;letter-spacing:.5px;background:#fff}

/* footer */
.site-footer{position:absolute;left:0;top:4290px;width:1200px;height:122px;color:#fff;font-size:12px}
.site-footer h5{font-size:13px;font-weight:700;margin-bottom:14px}
.footer-links{position:absolute;left:153px;top:0}
.footer-links nav{display:flex;gap:10px;margin-bottom:6px}
.footer-links nav a{color:#fff;text-decoration:none}
.footer-links nav i{font-style:normal;opacity:.8}
.footer-contact{position:absolute;left:668px;top:0;width:330px}
.footer-contact .addr{display:flex;gap:8px;line-height:1.45}
.to-top{position:absolute;left:1140px;top:4312px;width:40px;height:40px;background:#fff;opacity:.85}
.to-top svg{display:block;margin:10px}
</style>
</head>
<body>

<section class="hero" role="img" aria-label="Ceiling dome security camera over a crowded concourse, tinted blue"></section>

<header class="site-header">
  <div class="brand">
    <span class="brand-mark"></span>
    <span class="brand-name">Lumora<br>Security Solutions</span>
  </div>
  <nav class="main-nav">
    <a class="active" href="#">HOME</a>
    <a href="#">ABOUT US</a>
    <a href="#">SERVICES</a>
    <a href="#">CONTACT US</a>
  </nav>
  <div class="call-btn">CALL: 1-1800-55-0142</div>
  <div class="social">
    <span aria-label="Chatterloop"></span>
    <span aria-label="Streamvue"></span>
  </div>
</header>

<h1 class="hero-title">SAFETY &amp; SECURITY</h1>
<p class="hero-copy">Comprehensive security systems including intrusion detection, access control, video surveillance, fire detection, and 24/7 monitoring.</p>
<div class="outline-btn" style="left:153px;top:414px">INQUIRY NOW</div>
<div class="hero-arrow" style="left:16px"><svg width="20" height="20" viewBox="0 0 20 20"><path d="M17 10H4M9 5l-5 5 5 5" stroke="#1a63c9" stroke-width="2.5" fill="none"/></svg></div>
<div class="hero-arrow" style="left:1144px"><svg width="20" height="20" viewBox="0 0 20 20"><path d="M3 10h13M11 5l5 5-5 5" stroke="#1a63c9" stroke-width="2.5" fill="none"/></svg></div>

<section class="support-bar">
  <svg class="abs" style="left:152px;top:24px" width="52" height="52" viewBox="0 0 52 52"><circle cx="26" cy="26" r="23" fill="none" stroke="#4d97ee" stroke-width="3"/><path d="M14 28v-4a12 12 0 0 1 24 0v4M14 27h4v8h-4zM34 27h4v8h-4z" fill="none" stroke="#4d97ee" stroke-width="3"/></svg>
  <h3>24/7 Customer Service &amp; Support</h3>
  <p>We are a local supplier in the community. We like to help you.</p>
  <svg class="abs" style="left:690px;top:36px" width="16" height="26" viewBox="0 0 16 26"><path d="M3 3l10 10L3 23" stroke="#fff" stroke-width="3" fill="none"/></svg>
  <div class="support-call">Call Us
    <svg width="20" height="20" viewBox="0 0 20 20" style="vertical-align:-3px"><circle cx="10" cy="10" r="9" fill="none" stroke="#5aa0f2" stroke-width="1.6"/><path d="M7 5l2 3-1.2 1.2a6 6 0 0 0 3 3L12 11l3 2-1 2c-4 0-9-5-9-9z" fill="#5aa0f2"/></svg>
    1-300-555-0199</div>
  <div class="support-mail">support@lumorasecurity.example</div>
</section>

<section class="about">
  <div class="about-backer"></div>
  <div class="about-photo" role="img" aria-label="Security operator on the phone at a desk watching a wall of monitors"></div>
  <h2><b>About</b> Our Company</h2>
  <p style="top:824px">Lorem ipsum dolor sit amet, consectetur adipiscing elit, sed do eiusmod tempor incididunt ut labore et dolore magna aliqua. Ut enim ad minim veniam lorem ipsum dolor sit amet, consectetur adipiscing elit, sed do eiusmod tempor incididunt ut labore et dolore magna aliqua. Ut enim ad minim veniam lorem ipsum dolor sit amet, consectetur adipiscing elit, sed do eiusmod tempor incididunt ut labore et dolore magna aliqua. Ut enim ad minim veniam lorem ipsum dolor sit amet, consectetur adipiscing elit, sed do eiusmod tempor incididunt ut labore et dolore magna aliqua.</p>
  <p style="top:1034px">Lorem ipsum dolor sit amet, consectetur adipiscing elit, sed do eiusmod tempor incididunt ut labore et dolore magna</p>
  <div class="blue-btn" style="left:661px;top:1112px">ABOUT US</div>
</section>

<h2 class="section-title"><b>Our</b> Services</h2>

<section class="service-row" style="top:1352px">
  <div class="service-photo" role="img" aria-label="Row of white dome and bullet CCTV cameras" style="left:140px;top:128px;width:350px;height:120px;background:linear-gradient(90deg,#e4e6e9,#c3c8cf 50%,#e9ebee);border-radius:40px"></div>
  <div class="service-text mint" style="left:600px">
    <div class="rule" style="left:-20px;width:260px"></div>
    <h3 style="left:61px">CCTV</h3>
    <p style="left:61px">Closed circuit television (CCTV) has long been implemented by businesses as a surveillance tool in areas that need monitoring. With digital CCTV cameras, multiple video cameras transmit signals through a set of monitors. The cameras provide thorough</p>
    <div class="blue-btn" style="left:61px">LEARN MORE</div>
  </div>
</section>

<section class="service-row" style="top:1755px">
  <div class="service-text sky" style="left:0">
    <div class="rule" style="left:74px;width:546px"></div>
    <h3 style="left:103px">Security Alarms</h3>
    <p style="left:103px">Alarms systems are electronic devices programmed to alert people to specific dangers and detect intrusions, fire or theft. Security alarms, systems and access control monitoring combine to create an integrated surveillance solution, tailored to your business' unique requirements.</p>
    <div class="blue-btn" style="left:103px">LEARN MORE</div>
  </div>
  <div class="service-photo" role="img" aria-label="Alarm control panel, keypads and motion sensors" style="left:700px;top:128px;width:380px;height:150px;background:linear-gradient(90deg,#e9edf2,#cfd8e4 50%,#eef1f5)"></div>
</section>

<section class="service-row" style="top:2158px">
  <div class="service-photo" role="img" aria-label="Fingerprint access control terminal" style="left:285px;top:110px;width:130px;height:185px;background:linear-gradient(180deg,#c9ccd1,#3b3e44 70%,#8b8f95)"></div>
  <div class="service-text mint" style="left:600px">
    <div class="rule" style="left:-20px;width:260px"></div>
    <h3 style="left:61px">Access Control</h3>
    <p style="left:61px">An access control system allows for the free flow of authorised personnel while denying entry to unwanted visitors. With walk-in thieves and trespassers shut out, you dramatically reduce your exposure to crime while increasing the security of your employees, visitors, information and assets.</p>
    <div class="blue-btn" style="left:61px">LEARN MORE</div>
  </div>
</section>

<section class="service-row" style="top:2561px">
  <div class="service-text sky fire" style="left:0">
    <div class="rule" style="left:74px;width:546px"></div>
    <h3 style="left:103px">Fire Protection</h3>
    <p style="left:103px">Back to base fire monitoring service 24 hours a day, 7 days a week.<br><br>We know how important it is to protect your building from fire and a simple solution is Fire Monitoring. We provide fire monitoring to every type of building and business, from the smallest neighbourhood shop to the largest retail centres, from workshops to warehouses, from carparks to large buildings.</p>
    <div class="blue-btn" style="left:103px">LEARN MORE</div>
  </div>
  <div class="service-photo" role="img" aria-label="Group of red fire extinguishers" style="left:750px;top:110px;width:230px;height:170px;background:linear-gradient(90deg,#c4262b,#e0474a 50%,#a81d22);border-radius:20px 20px 6px 6px"></div>
</section>

<div class="dash" style="left:384px;width:150px"></div>
<div class="dash" style="left:666px;width:150px"></div>
<div class="feature" style="left:184px">
  <div class="feature-icon"><svg width="64" height="64" viewBox="0 0 64 64" fill="none" stroke="#2b2e33" stroke-width="2.5"><circle cx="32" cy="16" r="7"/><circle cx="14" cy="40" r="6"/><circle cx="50" cy="40" r="6"/><path d="M4 60c0-7 5-11 10-11s10 4 10 11M40 60c0-7 5-11 10-11s10 4 10 11M22 34l-4 2M42 34l4 2"/></svg></div>
  <h4>Experienced Team</h4>
</div>
<div class="feature" style="left:490px">
  <div class="feature-icon primary"><svg width="62" height="62" viewBox="0 0 64 64" fill="none" stroke="#fff" stroke-width="2.5"><rect x="6" y="8" width="30" height="20" rx="3"/><rect x="28" y="24" width="30" height="20" rx="3"/><circle cx="26" cy="50" r="6"/><path d="M16 62c0-6 4-8 10-8s10 2 10 8"/></svg></div>
  <h4 class="accent">[ 24x7 Support ]</h4>
</div>
<div class="feature" style="left:796px">
  <div class="feature-icon"><svg width="64" height="64" viewBox="0 0 64 64" fill="none" stroke="#2b2e33" stroke-width="2.5"><rect x="6" y="10" width="52" height="36" rx="3"/><path d="M24 56h16M32 46v10"/><text x="32" y="34" text-anchor="middle" font-family="Open Sans,sans-serif" font-size="13" font-weight="700" fill="#2b2e33" stroke="none">LIVE</text></svg></div>
  <h4>Live System Updates</h4>
</div>

<section class="cta-band">
  <h2>We are one of reliable Security System Provider.</h2>
  <p>Looking to make your Business or Home Secure with Technology!</p>
  <div class="outline-btn" style="left:514px;top:142px">CONSULT NOW</div>
</section>

<div class="map-area" role="img" aria-label="Street map showing the office location along the coast"></div>
<svg class="abs" style="left:746px;top:3654px" width="26" height="36" viewBox="0 0 26 36"><path d="M13 35C5 23 2 18 2 12a11 11 0 0 1 22 0c0 6-3 11-11 23z" fill="#d9332b"/><circle cx="13" cy="12" r="4" fill="#8e1c16"/></svg>

<div class="blue-foot"></div>

<section class="contact-card">
  <h2>Contact Us Today</h2>
  <p class="lead">Got a question? Send us a message and we'll respond as soon as possible.</p>
  <div class="field" style="left:82px;top:118px;width:256px">Name</div>
  <div class="field" style="left:353px;top:118px;width:259px">Email</div>
  <div class="field" style="left:626px;top:118px;width:197px">Phone</div>
  <div class="field message" style="left:82px;top:168px;width:741px">Type your Message ...</div>
  <div class="send-btn">SEND MESSAGE</div>
</section>

<footer class="site-footer">
  <div class="footer-links">
    <h5>Quick Links</h5>
    <nav><a href="#">Home</a><i>|</i><a href="#">About us</a><i>|</i><a href="#">Services</a><i>|</i><a href="#">Contact us</a></nav>
    <p>© 2018 Lumora Security Solutions</p>
  </div>
  <div class="footer-contact">
    <h5>Lumora Security Solutions</h5>
    <div class="addr">
      <svg width="14" height="18" viewBox="0 0 14 18"><path d="M7 17C2 11 1 8.5 1 6a6 6 0 0 1 12 0c0 2.5-1 5-6 11z" fill="#fff"/><circle cx="7" cy="6" r="2.2" fill="#1752b2"/></svg>
      <span>Lumora Security Solutions, Harlow Road,<br>Westbrook NSW, Australia.</span>
    </div>
  </div>
</footer>
<div class="to-top"><svg width="20" height="20" viewBox="0 0 20 20"><path d="M10 16V4M5 9l5-5 5 5" stroke="#1a63c9" stroke-width="2.5" fill="none"/></svg></div>

</body>
</html>
```